Bright Paddock Learning Program with the aim of promoting a skills football to school aged children to

Need an A5 back to front one page brochure which is colourful, fun and active to attract the students to purchase the football with part of the funds going back to the school.
Whole idea is to get more footballs in the hands of children of primary school age, fo the school to earn funds from the sale as well as us also making some funds from the sale.
Target Market(s)
5-11 Year old boys and girls
Industry/Entity Type
School
Colors
219ed3
ffffff
0255a3
33b8a4
ec1f27
Requirements
Must have
- Must have football, price, promotional words as per example and contact details of who is ordering the footballs.
- Have included a version we have done up but are not happy with, needs to be much more professional than the attachment to the brief.
Nice to have
- Promotional component on the front with plenty of colours and attraction, with detail requirements on the back
Should not have
- No soccer or KRB balls, only Aussie Rules Footballs in design

```html
<!DOCTYPE html>
<html lang="en">
<head>
<meta charset="utf-8">
<title>Bright Paddock Learning Program – Footies for School</title>
<link rel="stylesheet" href="https://fonts.googleapis.com/css2?family=Arvo:wght@400;700&family=Bebas+Neue&family=Roboto+Slab:wght@400;700&display=swap">
<style>
  :root{
    --stage:#3d3d3d;
    --sky:#219ed3;
    --navy:#0255a3;
    --teal:#33b8a4;
    --red:#ec1f27;
    --white:#ffffff;
    --ink:#111111;
    --grass:#4f9a1f;
    --grass-light:#7fc826;
    --leaf:#4a8a1c;
    --form-ink:#1d3d5c;
  }
  *{margin:0;padding:0;box-sizing:border-box}
  html,body{width:1200px;height:834px;overflow:hidden;background:var(--stage)}
  .stage{position:relative;width:1200px;height:834px}
  .page{position:absolute;top:85px;width:479px;height:680px;overflow:hidden;box-shadow:0 3px 10px rgba(0,0,0,.45)}
  .page--front{left:88px;background:linear-gradient(180deg,#1f6aa0 0%,#2a7f8e 40%,#3f9a4e 70%,#4aa232 100%)}
  .page--back{left:613px;background:linear-gradient(180deg,#4e8f1c 0%,#5a9a2a 30%,#5b9bb4 65%,#6a9fd6 100%)}

  .rays{position:absolute;inset:0;background:radial-gradient(circle at 65% 55%,rgba(255,255,255,.18),rgba(255,255,255,0) 60%)}

  /* front */
  .title-banners{position:absolute;left:0;top:0;width:479px;height:340px}
  .title-banners text{font-family:"Arvo",serif;font-weight:700;fill:var(--white)}
  .price-badge{position:absolute;left:19px;top:331px;width:134px;height:134px}
  .price-badge text{font-family:"Bebas Neue",sans-serif;fill:var(--red);text-anchor:middle}
  .photo-kid-kick{position:absolute;left:175px;top:130px;width:300px;height:520px;border-radius:140px 140px 20px 20px;
    background:linear-gradient(180deg,rgba(230,150,60,.55),rgba(220,130,40,.55) 60%,rgba(190,40,40,.4))}
  .grass{position:absolute;left:0;bottom:0;width:479px;height:142px;background:linear-gradient(180deg,rgba(127,200,38,0),var(--grass-light) 45%,var(--leaf))}
  .perks{position:absolute;left:32px;top:502px;width:330px;list-style:none;font-family:"Roboto Slab",serif;color:var(--white)}
  .perks li{position:relative;padding-left:30px;font-size:10px;line-height:14px;margin-bottom:13px}
  .perks li::before{content:"";position:absolute;left:0;top:2px;width:19px;height:19px;border-radius:50%;background:var(--red);box-shadow:0 0 0 2px rgba(255,255,255,.6)}
  .perks strong{display:block;font-size:11.5px;line-height:15px;font-weight:700}
  .commission{position:absolute;left:285px;top:560px;width:180px;text-align:center;font-family:"Roboto Slab",serif;color:var(--ink)}
  .commission-mark{width:44px;height:44px;border-radius:50%;background:var(--ink);margin:0 auto 8px}
  .commission-name{font-size:9px;line-height:12px;font-weight:700;text-transform:uppercase}

  /* back */
  .frame{position:absolute;left:25px;top:22px;width:425px;height:631px;border:1px dashed rgba(40,40,40,.6)}
  .lead{position:absolute;left:55px;top:40px;font-family:"Arvo",serif;font-size:25px;color:var(--white);letter-spacing:.3px}
  .headline{position:absolute;left:53px;top:70px;font-family:"Bebas Neue",sans-serif;color:var(--white);line-height:.92}
  .headline .big{display:block;font-size:66px}
  .headline .mid{display:block;font-size:50px}
  .photo-kid-catch{position:absolute;left:40px;top:280px;width:380px;height:400px;border-radius:190px 190px 0 0;
    background:linear-gradient(180deg,rgba(150,80,50,.5),rgba(230,190,160,.45) 45%,rgba(120,80,50,.5) 80%,rgba(200,40,40,.6))}
  .order-panel{position:absolute;left:55px;top:169px;width:373px;height:211px;background:rgba(255,255,255,.28)}
  .order-inner{position:absolute;left:15px;top:15px;width:343px;height:182px;border:1px dashed rgba(120,30,30,.7);
    padding:14px 28px 0 22px;font-family:"Roboto Slab",serif;color:var(--form-ink)}
  .order-title{font-size:12.5px;margin-bottom:12px}
  .field{display:flex;align-items:flex-end;gap:6px;font-size:7.5px;text-transform:uppercase;height:24px;padding-bottom:2px}
  .field .line{flex:1;border-bottom:1px solid var(--navy);margin-bottom:2px}
  .field .short{flex:0 0 52px}
  .check{display:inline-block;width:10px;height:10px;border:1px solid var(--form-ink);background:var(--white);margin:0 3px 0 6px;vertical-align:-2px}
  .office{font-weight:700}
  .social{position:absolute;left:194px;top:584px;display:flex;gap:5px}
  .social span{width:24px;height:24px;border-radius:50%;background:var(--grass)}
</style>
</head>
<body>
<main class="stage">

  <section class="page page--front" aria-label="Front of flyer">
    <div class="rays"></div>
    <div class="photo-kid-kick" role="img" aria-label="Photo of a young boy in an orange club jersey holding a yellow Aussie Rules football"></div>
    <div class="grass" role="img" aria-label="Green grass along the bottom edge"></div>

    <svg class="title-banners" viewBox="0 0 479 340" aria-label="Footies for School">
      <polygon points="19,83 356,20 340,104 7,165" fill="var(--red)"/>
      <text x="40" y="150" font-size="58" transform="rotate(-10 40 150)">FOOTIES</text>
      <polygon points="44,161 192,136 175,206 21,234" fill="var(--ink)"/>
      <text x="52" y="218" font-size="48" transform="rotate(-10 52 218)">FOR</text>
      <polygon points="48,239 270,190 257,276 19,323" fill="var(--red)"/>
      <text x="50" y="305" font-size="44" transform="rotate(-12 50 305)">SCHOOL</text>
    </svg>

    <svg class="price-badge" viewBox="0 0 134 134" aria-label="Just $17 each">
      <circle cx="67" cy="67" r="66" fill="var(--white)"/>
      <circle cx="67" cy="67" r="59" fill="#eeeeee" stroke="var(--red)" stroke-width="1.5" stroke-dasharray="6 3"/>
      <text x="67" y="41" font-size="24">JUST</text>
      <text x="67" y="97" font-size="66">$17</text>
      <text x="67" y="120" font-size="18">EACH</text>
    </svg>

    <ul class="perks">
      <li><strong>Order your own exclusive* 12” Skill Football in your local CJFL club colours</strong>&amp; improve your technique this season<br>&amp; help fundraise money for your school.</li>
      <li>All orders delivered in Term 2 just in<br>time for footy season.</li>
      <li>$5 from each football purchased will<br>go straight back to your schools P&amp;C!</li>
    </ul>

    <div class="commission">
      <div class="commission-mark"></div>
      <div class="commission-name">Coastal Junior Football Commission</div>
    </div>
  </section>

  <section class="page page--back" aria-label="Back of flyer">
    <div class="rays"></div>
    <div class="photo-kid-catch" role="img" aria-label="Photo from behind of a boy raising both hands to catch an Aussie Rules football"></div>
    <div class="frame"></div>

    <p class="lead">when you buy football from us</p>
    <h1 class="headline"><span class="big">PART OF THE FUNDS</span><span class="mid">GOES BACK TO THE SCHOOL</span></h1>

    <div class="order-panel">
      <form class="order-inner">
        <p class="order-title">ORDER INFORMATION</p>
        <div class="field">Student name <span class="line"></span></div>
        <div class="field">Year <span class="line short"></span> Class room <span class="line"></span></div>
        <div class="field">Number of footballs <span class="line"></span></div>
        <div class="field">Payment method <span class="check"></span>Cash <span class="check"></span>Cheque <span class="check"></span>EFT</div>
        <div class="field office">Office only</div>
        <div class="field">Payment received <span class="line"></span></div>
      </form>
    </div>

    <div class="social" aria-label="Social links"><span></span><span></span><span></span></div>
  </section>

</main>
</body>
</html>
```